Lawn Sign For Construction Projects - Vantor Power

This contest is for a lawn sign that will be placed in the front yard of recently completed construction projects. The goal here is to have a bold advertising sign that is visible from a vehicle driving past.

We are still deciding on the default size for our sign, we also may use multiple sizes. The two sizes we will more than likely be using are: 18"h x 24"w and 24"h x 36"w.

Preference will be given to designers that submit original designs that tie into our current brand and are either in both the size formats listed above or are easy to scale in photoshop or illustrator.

In the files, you will see our logo and an example of a lawn sign.

Please contact us with any questions or comments you may have!

Thank You,
- The Vantor Power Team

Industry/Entity Type

Residential Construction

Colors
34a7d8
ffffff
faa54b

Requirements
Nice to have
• 1. The sign must tie into our current branding and color scheme.
• 2. The sign must be clearly visible and readable.
• 3. The sign must include our phone number in readable print.
• 4. Our website written in small print along the bottom of the sign.
• 5. Must mention we install the following products:
• a.) Solar
• b.) Roofing
• c.) Windows
• d.) Artificial Lawn
• e.) Whole House Fans
• f.) Patio Covers

```html
<!DOCTYPE html>
<html lang="en">
<head>
<meta charset="utf-8">
<title>Vantor Power – Lawn Sign</title>
<link rel="stylesheet" href="https://fonts.googleapis.com/css2?family=Montserrat:wght@500;700&family=Arimo:wght@400;700&display=swap">
<style>
  :root {
    --cream: #f7f6d9;
    --wave-pale: #eef0b4;
    --wave-mid: #dfe68c;
    --field-light: #b7d54e;
    --field-deep: #93c23a;
    --grass-light: #9fcd3c;
    --grass-deep: #5f9f22;
    --brand-blue: #34a7d8;
    --brand-orange: #faa54b;
    --ink: #1f2a44;
    --white: #ffffff;
    --arrow-fill: #d7e85a;
    --arrow-line: #3d5a14;
  }
  * { margin: 0; padding: 0; box-sizing: border-box; }
  html, body { width: 1200px; height: 900px; overflow: hidden; background: var(--cream); }
  .sign {
    position: relative;
    width: 1200px;
    height: 900px;
    overflow: hidden;
    background: var(--cream);
    font-family: "Arimo", Arial, sans-serif;
  }
  .sign__waves { position: absolute; inset: 0; width: 1200px; height: 900px; }
  .sign__grass-top {
    position: absolute; left: 0; top: 0; width: 1200px; height: 150px;
    background: linear-gradient(to bottom, var(--grass-deep) 0%, #7cb832 45%, rgba(160,205,70,0.55) 75%, rgba(247,246,217,0) 100%);
  }
  .sign__grass-bottom {
    position: absolute; left: 0; bottom: 0; width: 1200px; height: 170px;
    background: linear-gradient(to bottom, rgba(159,205,60,0) 0%, var(--grass-light) 30%, #7fb92e 70%, var(--grass-deep) 100%);
  }
  .brand {
    position: absolute; left: 690px; top: 190px; width: 480px;
    text-align: center;
  }
  .brand__dot {
    display: block; width: 116px; height: 116px; margin: 0 auto 36px;
    border-radius: 50%; background: var(--brand-orange);
  }
  .brand__name {
    font-family: "Montserrat", Arial, sans-serif;
    font-weight: 700; font-size: 54px; line-height: 1;
    color: var(--brand-blue); letter-spacing: 0.5px;
    text-transform: uppercase;
  }
  .brand__phone {
    margin-top: 22px;
    font-family: "Montserrat", Arial, sans-serif;
    font-weight: 500; font-size: 34px; line-height: 1;
    color: var(--ink); letter-spacing: 5px;
  }
  .services {
    position: absolute; left: 118px; top: 562px;
    list-style: none;
  }
  .services__item {
    display: flex; align-items: center;
    height: 50px;
    font-size: 25px; color: var(--white);
    text-shadow: 0 1px 2px rgba(40,70,10,0.35);
  }
  .services__arrow { width: 34px; height: 24px; margin-right: 18px; flex: none; }
  .site {
    position: absolute; right: 52px; bottom: 14px;
    font-family: "Arimo", Arial, sans-serif;
    font-weight: 700; font-size: 21px; letter-spacing: 2px;
    color: var(--white); text-transform: uppercase;
  }
</style>
</head>
<body>
<main class="sign">
  <svg class="sign__waves" viewBox="0 0 1200 900" aria-hidden="true">
    <defs>
      <linearGradient id="fieldGradient" x1="0" y1="0" x2="0" y2="1">
        <stop offset="0" stop-color="#c2da58"/>
        <stop offset="1" stop-color="#93c23a"/>
      </linearGradient>
    </defs>
    <path d="M0,170 C320,190 640,330 1200,520 L1200,900 L0,900 Z" fill="var(--wave-pale)"/>
    <path d="M0,300 C360,330 720,430 1200,560 L1200,900 L0,900 Z" fill="var(--wave-mid)"/>
    <path d="M0,460 C320,480 660,560 1200,640 L1200,900 L0,900 Z" fill="url(#fieldGradient)"/>
    <path d="M320,650 C640,570 960,580 1200,600 L1200,660 C950,645 640,640 320,668 Z" fill="#eef2a8" opacity="0.6"/>
  </svg>

  <div class="sign__grass-top" role="img" aria-label="Fresh green grass blades along the top edge"></div>
  <div class="sign__grass-bottom" role="img" aria-label="Green lawn grass along the bottom edge"></div>

  <header class="brand">
    <span class="brand__dot" aria-hidden="true"></span>
    <h1 class="brand__name">Vantor Power</h1>
    <p class="brand__phone">0800-555-0142</p>
  </header>

  <ul class="services">
    <li class="services__item"><svg class="services__arrow" viewBox="0 0 34 24" aria-hidden="true"><path d="M2,8 H18 V2 L32,12 L18,22 V16 H2 Z" fill="var(--arrow-fill)" stroke="var(--arrow-line)" stroke-width="2" stroke-linejoin="round"/></svg>Solar</li>
    <li class="services__item"><svg class="services__arrow" viewBox="0 0 34 24" aria-hidden="true"><path d="M2,8 H18 V2 L32,12 L18,22 V16 H2 Z" fill="var(--arrow-fill)" stroke="var(--arrow-line)" stroke-width="2" stroke-linejoin="round"/></svg>Roofing</li>
    <li class="services__item"><svg class="services__arrow" viewBox="0 0 34 24" aria-hidden="true"><path d="M2,8 H18 V2 L32,12 L18,22 V16 H2 Z" fill="var(--arrow-fill)" stroke="var(--arrow-line)" stroke-width="2" stroke-linejoin="round"/></svg>Windows</li>
    <li class="services__item"><svg class="services__arrow" viewBox="0 0 34 24" aria-hidden="true"><path d="M2,8 H18 V2 L32,12 L18,22 V16 H2 Z" fill="var(--arrow-fill)" stroke="var(--arrow-line)" stroke-width="2" stroke-linejoin="round"/></svg>Artificial Lawn</li>
    <li class="services__item"><svg class="services__arrow" viewBox="0 0 34 24" aria-hidden="true"><path d="M2,8 H18 V2 L32,12 L18,22 V16 H2 Z" fill="var(--arrow-fill)" stroke="var(--arrow-line)" stroke-width="2" stroke-linejoin="round"/></svg>Whole House Fans</li>
    <li class="services__item"><svg class="services__arrow" viewBox="0 0 34 24" aria-hidden="true"><path d="M2,8 H18 V2 L32,12 L18,22 V16 H2 Z" fill="var(--arrow-fill)" stroke="var(--arrow-line)" stroke-width="2" stroke-linejoin="round"/></svg>Patio Covers</li>
  </ul>

  <p class="site">www.vantorpower.com</p>
</main>
</body>
</html>
```